need eczema bath soak label/bag

need you to recreate this please. ai file. recreate this exact image please. ...if you want a big tip, create some different styles.

Colors
0054AA
0677BA
7BADD7
CADEEF
E8F1F8

```html
<!DOCTYPE html>
<html lang="en">
<head>
<meta charset="utf-8">
<title>The Ocean Healed Soak – Bath Soak Label</title>
<link rel="stylesheet" href="https://fonts.googleapis.com/css2?family=Outfit:wght@300;400;600;800&display=swap">
<style>
  :root {
    --stage: #022e2f;
    --ink: #03383a;
    --sky: #ffffff;
    --sea-deep: #35b6b8;
    --sea-light: #7fd3cd;
    --foam: #f4f7f7;
    --wet-sand: #ddd2cc;
    --sand: #e8d5a9;
    --sand-deep: #dcc493;
  }
  * { box-sizing: border-box; margin: 0; padding: 0; }
  html, body {
    width: 1200px; height: 888px; overflow: hidden;
    background: var(--stage);
  }
  .stage {
    position: relative; width: 1200px; height: 888px;
    display: flex; justify-content: center; align-items: center;
  }
  .label {
    position: relative; width: 533px; height: 888px; overflow: hidden;
    font-family: "Outfit", sans-serif; color: var(--ink); text-align: center;
  }
  .label__scene {
    position: absolute; inset: 0;
    background: linear-gradient(180deg,
      var(--sky) 0%, var(--sky) 22%,
      var(--sea-light) 27%, var(--sea-deep) 33%, var(--sea-deep) 39%,
      var(--sea-light) 44%, var(--foam) 49%, var(--foam) 55%,
      var(--wet-sand) 60%, var(--wet-sand) 69%,
      var(--sand) 75%, var(--sand-deep) 88%, var(--sand) 100%);
  }
  .label__content { position: absolute; inset: 0; }
  .title-the {
    position: absolute; top: 94px; left: 0; right: 0;
    font-weight: 800; font-size: 33px; letter-spacing: 0.5px; line-height: 1;
  }
  .title-main {
    position: absolute; top: 140px; left: 0; right: 0;
    font-weight: 800; font-size: 78px; line-height: 82px; letter-spacing: -0.5px;
  }
  .claim {
    position: absolute; top: 398px; left: 0; right: 0;
    font-weight: 300; font-size: 17.5px; line-height: 22.5px;
  }
  .treatment {
    position: absolute; top: 483px; left: 0; right: 0;
    font-weight: 600; font-size: 21px; letter-spacing: -0.2px;
  }
  .weight {
    position: absolute; top: 515px; left: 0; right: 0;
    font-weight: 600; font-size: 26px;
    transform: rotate(-2deg);
  }
  .product-type {
    position: absolute; top: 560px; left: 0; right: 0;
    font-weight: 300; font-size: 18px; letter-spacing: 0.2px;
  }
  .brand {
    position: absolute; top: 708px; left: 0; right: 0;
    display: flex; flex-direction: column; align-items: center; gap: 14px;
  }
  .brand__mark { width: 34px; height: 34px; background: var(--ink); }
  .brand__name {
    font-weight: 600; font-size: 15px; letter-spacing: 4px;
  }
</style>
</head>
<body>
<main class="stage">
  <article class="label">
    <div class="label__scene" role="img" aria-label="Aerial photograph of a turquoise ocean wave washing onto a sandy beach"></div>
    <div class="label__content">
      <p class="title-the">THE</p>
      <h1 class="title-main">OCEAN<br>HEALED<br>SOAK</h1>
      <p class="claim">bath soak to relieve symptoms<br>of mid exzema &amp; itchy, irritated,<br>dry skin</p>
      <p class="treatment">SOOTHING TREATMENT</p>
      <p class="weight">170g/60oz</p>
      <p class="product-type">BATH SOAK</p>
      <div class="brand">
        <span class="brand__mark"></span>
        <span class="brand__name">TIDEWELL</span>
      </div>
    </div>
  </article>
</main>
</body>
</html>
```